Business cards for Norwegian software consultancy business

We are in need of business cards for our Norwegian consultancy company.
“Talvik Brensor AS” specializes in software development, architecture and agile methodology, providing mostly on-site services at customers.
The cards should reflect a certain level of business professionalism with an elegant touch, while paying tribute to our modern and technological heritage. Our logo should be featured, as well as room for basic information about the cardholder and legal information of the company (company name, address and VAT number).
We would like our cards to reflect that we are a modern consulting company. It should present a professional image that people will remember. The texture and color pallette should reflect our professionalism and reliability, so we prefer a light color pallette with colors such as gray, white, blue and black. The number of colors used should however not be overwhelming, with the text being distinct and readable.
We are open to untraditional layouts and playful designs as long as they communicate the intent stated above.
You could also take a look at our website http://www.brensor.no for input on our visual profile.
Our logo is attached in the form of vectors and rasterized PNG. Please comment if you would like the black-white and/or inverted versions as well.
Architecture
Company information:
Talvik Brensor AS
Lindeholtveien 7, 3142 Vestskogen
461 82 915
info@brensor.no
www.brensor.no
Employee information:
Full name
Title
Email
Phone

```html
<!DOCTYPE html>
<html lang="no">
<head>
<meta charset="utf-8">
<title>Talvik Brensor AS – Visittkort</title>
<link rel="stylesheet" href="https://fonts.googleapis.com/css2?family=Montserrat:wght@600&family=Questrial&display=swap">
<style>
  :root {
    --page-bg: #e9ecef;
    --card-white: #ffffff;
    --ink: #1d1d1f;
    --ink-soft: #333538;
    --ink-muted: #6a6d72;
    --rule: #2a2a2a;
    --icon-bg: #2b2b2d;
    --blue-sky: #9fd8f4;
    --blue-mid: #4a9cd8;
    --blue-soft: #7ba7da;
    --blue-bright: #34b6ea;
    --brand-blue: #3b8fd0;
  }
  * { box-sizing: border-box; margin: 0; padding: 0; }
  html, body {
    width: 1200px; height: 1200px; overflow: hidden;
    background: var(--page-bg);
    font-family: "Questrial", "Century Gothic", sans-serif;
    color: var(--ink);
  }
  .business-card {
    position: absolute; left: 80px; top: 263px;
    width: 1040px; height: 673px;
    background: var(--card-white);
    box-shadow: 0 6px 18px rgba(0,0,0,.18);
    overflow: hidden;
  }
  .card-art {
    position: absolute; left: 0; top: 0; width: 572px; height: 673px;
    background: linear-gradient(135deg, var(--blue-sky) 0%, var(--blue-mid) 45%, var(--blue-soft) 70%, var(--blue-bright) 100%);
  }
  .brand-band {
    position: absolute; left: 0; top: 292px; width: 480px; height: 84px;
    background: var(--card-white);
    display: flex; align-items: center; justify-content: flex-end;
    padding-right: 40px; gap: 16px;
  }
  .brand-mark { width: 24px; height: 24px; background: var(--brand-blue); }
  .brand-name { font-size: 34px; letter-spacing: 1px; color: var(--brand-blue); }
  .band-bar { position: absolute; background: var(--card-white); }
  .band-bar.wide { left: 492px; top: 268px; width: 10px; height: 130px; }
  .band-bar.thin { left: 510px; top: 280px; width: 5px; height: 106px; }

  .holder { position: absolute; right: 72px; top: 108px; text-align: right; }
  .holder-name { font-size: 26px; letter-spacing: .5px; color: var(--ink); }
  .holder-name strong { font-family: "Montserrat", sans-serif; font-weight: 600; }
  .holder-title { font-size: 20px; color: var(--ink-soft); margin-top: 2px; }

  .contact-list { position: absolute; left: 606px; top: 392px; width: 386px; list-style: none; }
  .contact-row {
    position: relative; border-top: 1.5px solid var(--rule);
    min-height: 58px; padding: 6px 0 6px 44px; text-align: right;
    font-size: 17px; line-height: 22px; color: var(--ink-soft);
  }
  .contact-icon {
    position: absolute; left: 0; top: 10px; width: 28px; height: 28px;
    background: var(--icon-bg); display: flex; align-items: center; justify-content: center;
  }
  .contact-icon svg { width: 16px; height: 16px; }
  .legal-line {
    position: absolute; left: 606px; top: 628px; width: 386px;
    text-align: right; font-size: 13px; letter-spacing: .3px; color: var(--ink-muted);
  }
</style>
</head>
<body>
  <main class="business-card">
    <div class="card-art" role="img" aria-label="Abstrakt mønster av overlappende blå flater"></div>
    <div class="brand-band">
      <span class="brand-mark"></span>
      <span class="brand-name">Talvik Brensor</span>
    </div>
    <span class="band-bar wide"></span>
    <span class="band-bar thin"></span>

    <header class="holder">
      <p class="holder-name">JONAS <strong>RAVNLI</strong></p>
      <p class="holder-title">Consultant</p>
    </header>

    <ul class="contact-list">
      <li class="contact-row">
        <span class="contact-icon"><svg viewBox="0 0 24 24"><path d="M12 2a7 7 0 0 0-7 7c0 5 7 13 7 13s7-8 7-13a7 7 0 0 0-7-7zm0 9.5A2.5 2.5 0 1 1 12 6.5a2.5 2.5 0 0 1 0 5z" fill="#fff"/></svg></span>
        Lindeholtveien 7, 3142 Vestskogen
      </li>
      <li class="contact-row">
        <span class="contact-icon"><svg viewBox="0 0 24 24"><path d="M6.6 10.8a15 15 0 0 0 6.6 6.6l2.2-2.2a1 1 0 0 1 1-.25 11.4 11.4 0 0 0 3.6.57 1 1 0 0 1 1 1V20a1 1 0 0 1-1 1A17 17 0 0 1 3 4a1 1 0 0 1 1-1h3.5a1 1 0 0 1 1 1c0 1.25.2 2.45.57 3.57a1 1 0 0 1-.25 1z" fill="#fff"/></svg></span>
        461 82 915<br>+47 - 918 - 44 206
      </li>
      <li class="contact-row">
        <span class="contact-icon"><svg viewBox="0 0 24 24"><path d="M3 5h18v14H3z" fill="#fff"/><path d="M3 5l9 7 9-7" fill="none" stroke="#2b2b2d" stroke-width="1.6"/></svg></span>
        info@brensor.no<br>jonasravnli@brensormail.no
      </li>
      <li class="contact-row">
        <span class="contact-icon"><svg viewBox="0 0 24 24"><g fill="none" stroke="#fff" stroke-width="1.6"><circle cx="12" cy="12" r="9"/><ellipse cx="12" cy="12" rx="4" ry="9"/><path d="M3 12h18M5 7h14M5 17h14"/></g></svg></span>
        www.brensor.no
      </li>
    </ul>
    <p class="legal-line">Talvik Brensor AS · Org.nr. 918 204 377 MVA</p>
  </main>
</body>
</html>
```